Menu sandwichbar

We have a sandwich bar and would like to change our menu.
The menu is a 3-panel folder with 6 printed sides.
We are looking for is original, quiet yet striking at the same time.
like black white newspaper style modern.

I have attached our current card. AND a screenshot with the style we want.

We have sandwiches, soup, pasta, pizza, salads and wraps.
So for each of these parts we need a breakdown.
I have also attached our logo.

We will need the file in EPS so we can add the dishes with the current price setting.

```html
<!DOCTYPE html>
<html lang="nl">
<head>
<meta charset="utf-8">
<title>Roadside Halt 14 – Menu folder</title>
<link rel="stylesheet" href="https://fonts.googleapis.com/css2?family=Montserrat:wght@400;700;800&family=Oswald:wght@600&display=swap">
<style>
  :root {
    --ink: #000000;
    --paper: #ffffff;
    --newsprint: #f4f1ea;
    --rust: #c9592a;
    --stage: #ffffff;
    --panel-w: 262px;
    --panel-h: 555px;
  }
  * { box-sizing: border-box; margin: 0; padding: 0; }
  html, body {
    width: 1097px; height: 1200px; overflow: hidden;
    background: var(--stage);
    font-family: "Montserrat", Arial, sans-serif;
  }
  .sheets {
    width: 1097px; height: 1200px;
    display: flex; flex-direction: column; align-items: center; justify-content: center;
    gap: 34px;
  }
  .spread { display: flex; width: calc(var(--panel-w) * 3); height: var(--panel-h); }
  .panel {
    width: var(--panel-w); height: var(--panel-h);
    padding: 27px 22px 0 32px;
    position: relative; overflow: hidden;
  }
  .panel--dark { background: var(--ink); color: var(--paper); --accent: var(--rust); --rule: var(--rust); }
  .panel--paper { background: var(--newsprint); color: var(--ink); --accent: var(--ink); --rule: var(--rust); }

  .menu-section + .menu-section { margin-top: 26px; }
  .section-title {
    font-weight: 700; font-size: 16px; line-height: 1.25;
    text-transform: uppercase; color: var(--accent);
    letter-spacing: 0.1px;
  }
  .rule { width: 56px; height: 3px; background: var(--rule); margin: 13px 0 8px; }
  .price-list { list-style: none; font-size: 11.6px; }
  .price-list li {
    display: flex; justify-content: space-between; gap: 8px;
    height: 14.6px; line-height: 14.6px; white-space: nowrap;
  }
  .price-list--spaced li { height: 16.3px; line-height: 16.3px; }
  .paninis { position: absolute; left: 32px; right: 22px; top: 372px; }
  .paninis .rule { margin: 13px 0 11px; }

  .cover { background: var(--ink); padding: 0; display: flex; flex-direction: column; align-items: center; }
  .brand {
    margin-top: 46px; display: flex; align-items: center; gap: 8px;
    font-weight: 800; font-size: 19px; color: var(--paper); text-transform: uppercase;
    letter-spacing: 0.4px; white-space: nowrap;
  }
  .brand-mark { width: 12px; height: 12px; background: var(--rust); flex: none; }
  .cover-photo {
    margin-top: 60px; width: 100%; height: 290px;
    background: linear-gradient(120deg, #1c1c1c 0%, #3a3a3a 45%, #c9a574 70%, #6f8d3c 100%);
  }
  .cover-contact {
    margin-top: 20px; text-align: center; font-style: normal;
    font-family: "Oswald", Arial, sans-serif; font-weight: 600; color: var(--rust);
    text-transform: uppercase;
  }
  .cover-contact .street { font-size: 15px; line-height: 20px; }
  .cover-contact .mail, .cover-contact .tel { font-size: 10px; line-height: 16px; }
  .cover-contact .tel { color: var(--paper); }
</style>
</head>
<body>
<main class="sheets">

  <!-- Outside spread -->
  <section class="spread spread--outside">
    <article class="panel panel--dark">
      <div class="menu-section">
        <h2 class="section-title">Soepen</h2>
        <div class="rule"></div>
        <ul class="price-list price-list--spaced">
          <li><span>Tomatensoep</span><span>€3,00</span></li>
          <li><span>Groentensoep</span><span>€3,00</span></li>
          <li><span>Kippensoep</span><span>€3,20</span></li>
          <li><span>Champignonsoep</span><span>€3,20</span></li>
          <li><span>Erwtensoep</span><span>€3,50</span></li>
          <li><span>Soep van de dag</span><span>€3,50</span></li>
        </ul>
      </div>
      <div class="menu-section">
        <h2 class="section-title">Salades</h2>
        <div class="rule"></div>
        <ul class="price-list price-list--spaced">
          <li><span>Salade kaas en ham</span><span>€7,50</span></li>
          <li><span>Salade kip curry</span><span>€8,00</span></li>
          <li><span>Salade tonijn</span><span>€8,50</span></li>
          <li><span>Salade geitenkaas</span><span>€9,00</span></li>
          <li><span>Salade caesar</span><span>€9,00</span></li>
          <li><span>Salade gerookte zalm</span><span>€9,50</span></li>
          <li><span>Salade scampi</span><span>€10,50</span></li>
        </ul>
      </div>
    </article>

    <article class="panel panel--paper">
      <div class="menu-section">
        <h2 class="section-title">Wraps</h2>
        <div class="rule"></div>
        <ul class="price-list price-list--spaced">
          <li><span>Wrap kip curry</span><span>€4,50</span></li>
          <li><span>Wrap kip samourai</span><span>€4,50</span></li>
          <li><span>Wrap tonijn</span><span>€4,80</span></li>
          <li><span>Wrap geitenkaas</span><span>€5,00</span></li>
          <li><span>Wrap gerookte zalm</span><span>€5,50</span></li>
          <li><span>Wrap falafel</span><span>€5,00</span></li>
        </ul>
      </div>
      <div class="menu-section">
        <h2 class="section-title">Pasta</h2>
        <div class="rule"></div>
        <ul class="price-list price-list--spaced">
          <li><span>Spaghetti bolognese</span><span>€8,50</span></li>
          <li><span>Spaghetti carbonara</span><span>€9,00</span></li>
          <li><span>Penne arrabbiata</span><span>€8,50</span></li>
          <li><span>Penne kip pesto</span><span>€9,50</span></li>
          <li><span>Tagliatelle zalm</span><span>€10,50</span></li>
          <li><span>Lasagne</span><span>€9,50</span></li>
          <li><span>Macaroni kaas en ham</span><span>€8,00</span></li>
        </ul>
      </div>
    </article>

    <article class="panel cover">
      <div class="brand"><span class="brand-mark"></span><span>Roadside Halt 14</span></div>
      <div class="cover-photo" role="img" aria-label="Photo of a filled baguette sandwich with lettuce, onion and corn on a dark wooden board"></div>
      <address class="cover-contact">
        <p class="street">Fabrieksstraat 8</p>
        <p class="street">2400 Veldhoven-Noord</p>
        <p class="mail">broodjes@roadsidehalt.eu</p>
        <p class="tel">T: 011 555 201 // F: 011/ 555 202</p>
      </address>
    </article>
  </section>

  <!-- Inside spread -->
  <section class="spread spread--inside">
    <article class="panel panel--dark">
      <h2 class="section-title">Traditionele brood<br>jeszonder groenten</h2>
      <div class="rule"></div>
      <ul class="price-list">
        <li><span>Broodje kaas</span><span>€3,00</span></li>
        <li><span>Broodje ham</span><span>€3,00</span></li>
        <li><span>Broodje salami</span><span>€3,00</span></li>
        <li><span>Broodje kaas en ham</span><span>€3,50</span></li>
        <li><span>Broodje vleessla</span><span>€3,50</span></li>
        <li><span>Broodje eiersla</span><span>€3,50</span></li>
        <li><span>Broodje kip hawai</span><span>€3,50</span></li>
        <li><span>Broodje kip curry</span><span>€3,50</span></li>
        <li><span>Broodje kip samourai</span><span>€3,50</span></li>
        <li><span>Broodje boulet met</span><span>€3,50</span></li>
        <li><span>Broodje préparé</span><span>€3,50</span></li>
        <li><span>Broodje martino</span><span>€3,70</span></li>
        <li><span>Broodje tonijnsla</span><span>€3,70</span></li>
        <li><span>Broodje krabsla</span><span>€4,20</span></li>
        <li><span>Broodje omelet met spek</span><span>€4,20</span></li>
        <li><span>Broodje brie</span><span>€4,20</span></li>
        <li><span>Broodje gerookte zalm</span><span>€4,70</span></li>
      </ul>
      <div class="paninis">
        <h2 class="section-title">Panini's</h2>
        <div class="rule"></div>
        <ul class="price-list price-list--spaced">
          <li><span>Paninikaas&amp;ham</span><span>€ 3,50</span></li>
          <li><span>Paninitraditioneel</span><span>€ 4,60</span></li>
          <li><span>Paniniparma</span><span>€ 5,00</span></li>
          <li><span>Paninibrie</span><span>€ 5,00</span></li>
          <li><span>Paninikip</span><span>€ 5,20</span></li>
          <li><span>Paniniboulet</span><span>€ 5,20</span></li>
        </ul>
      </div>
    </article>

    <article class="panel panel--paper">
      <h2 class="section-title">Broodjes met<br>groenten</h2>
      <div class="rule"></div>
      <ul class="price-list">
        <li><span>Broodje kaas</span><span>€3,50</span></li>
        <li><span>Broodje ham</span><span>€3,50</span></li>
        <li><span>Broodje kaas en ham</span><span>€4,00</span></li>
        <li><span>Broodje kip curry</span><span>€4,00</span></li>
        <li><span>Broodje kip hawai</span><span>€4,00</span></li>
        <li><span>Broodje tonijnsla</span><span>€4,20</span></li>
        <li><span>Broodje krabsla</span><span>€4,70</span></li>
        <li><span>Broodje brie</span><span>€4,70</span></li>
        <li><span>Broodje gerookte zalm</span><span>€5,20</span></li>
      </ul>
      <div class="paninis">
        <h2 class="section-title">Pizza</h2>
        <div class="rule"></div>
        <ul class="price-list price-list--spaced">
          <li><span>Pizza margherita</span><span>€ 8,00</span></li>
          <li><span>Pizza prosciutto</span><span>€ 9,00</span></li>
          <li><span>Pizza salami</span><span>€ 9,00</span></li>
          <li><span>Pizza hawai</span><span>€ 9,50</span></li>
          <li><span>Pizza quattro formaggi</span><span>€ 10,00</span></li>
          <li><span>Pizza tonno</span><span>€ 10,00</span></li>
        </ul>
      </div>
    </article>

    <article class="panel panel--dark">
      <h2 class="section-title">Warme<br>broodjes</h2>
      <div class="rule"></div>
      <ul class="price-list">
        <li><span>Broodje boulet tomaat</span><span>€4,20</span></li>
        <li><span>Broodje kip andalouse</span><span>€4,50</span></li>
        <li><span>Broodje gehakt ui</span><span>€4,50</span></li>
        <li><span>Broodje spek en ei</span><span>€4,50</span></li>
        <li><span>Broodje kaas gesmolten</span><span>€4,20</span></li>
        <li><span>Broodje shoarma</span><span>€5,00</span></li>
        <li><span>Broodje pulled pork</span><span>€5,50</span></li>
        <li><span>Broodje stoofvlees</span><span>€5,50</span></li>
        <li><span>Broodje scampi look</span><span>€6,00</span></li>
      </ul>
      <div class="paninis">
        <h2 class="section-title">Croques</h2>
        <div class="rule"></div>
        <ul class="price-list price-list--spaced">
          <li><span>Croque monsieur</span><span>€ 4,00</span></li>
          <li><span>Croque hawai</span><span>€ 4,50</span></li>
          <li><span>Croque bolognese</span><span>€ 5,00</span></li>
          <li><span>Croque brie honing</span><span>€ 5,00</span></li>
          <li><span>Croque kip curry</span><span>€ 5,20</span></li>
          <li><span>Croque zalm</span><span>€ 5,50</span></li>
        </ul>
      </div>
    </article>
  </section>

</main>
</body>
</html>
```